Corrimbel Lodge Web Design Project

I am looking for a striking, modern and user friendly site to promote my business, Corrimbel Lodge.

Corrimbel Lodge comprises of 3 elements : Restaurant, Resort and Events and the site must showcase all of these.
Updates

Project Deadline Extended
Reason: Too far away from brief ! Please check out the 2 website links to restaurant sites i LOVE for inspiration ! I am happy to pay for a quality designer and also for anyone that can code this !

Target Market(s)

Our Restaurant clientele demographic is 30-60 years old and are a mix of locals and tourists. The Restaurant is very much a destination venue so we attract people that wish to seek out amazing food.

The Event side of things attracts mainly weddings, this is a lucrative arm of the business and this side of the site must also be outstanding.

The Resort comprises of 7 boutique loft apartment and has a big pool and spa. We attract a mix of locals but want to push it as a ' getaway '

Industry/Entity Type

Business

Requirements
Must have
• I would like the first page to be an overall blog and to highlight the 3 area of the business. Lets have the 3 keywords as clickable tabs that take you to that section of the site.

RESTAURANT RESORT EVENTS

The RESTAURANT page should include the following tabs ( i have provided the information to be added to each tab as an example )

MENU ( Breakfast, Lunch, Dinner, Set Menu, Wine List)

FUNCTIONS (Private Dining Room, Exclusive Use, Wine Nights Coming Soon)

RESERVATIONS (Enquiry Form linked to my info@ address, Reservation Policies, Contact Number)

GALLERY & PRESS ( Press Articles, Latest News, What's On, Photo's, Wedding Hot Spot)

CONTACT US (Opening Times, Map, Contact Details, Sign Up For Our Newsletter, Facebook Link )

The RESORT page should include the following tabs :
# LOFTS & RATES
# FACILITIES
# SPECIAL OFFERS
# GALLERY
# RESERVATIONS

The EVENTS page should include the following tabs :
# WEDDINGS
# CONFERENCES
# PRIVATE EVENTS
# GALLERY
# ENQUIRY FORM
Nice to have
• Include Logo, good branding

```html
<!DOCTYPE html>
<html lang="en">
<head>
<meta charset="utf-8">
<title>Corrimbel Lodge – Breakfast Menu</title>
<link href="https://fonts.googleapis.com/css2?family=Questrial&family=Quicksand:wght@400;500&display=swap" rel="stylesheet">
<style>
  :root {
    --bg-dark: #2a1d14;
    --bg-mid: #6b5646;
    --bg-light: #bfb3a6;
    --sidebar: rgba(225, 210, 195, 0.72);
    --panel: rgba(214, 214, 214, 0.93);
    --tab-breakfast: #ffa300;
    --tab-dinner: #ff5a00;
    --tab-lunch: #d14a00;
    --tab-fold: #b84000;
    --accent: #ff5a00;
    --ink: #111111;
    --nav-ink: #1a1a1a;
    --white: #ffffff;
  }
  * { margin: 0; padding: 0; box-sizing: border-box; }
  html, body { width: 1200px; height: 1000px; overflow: hidden; }
  body { font-family: "Questrial", sans-serif; color: var(--ink); position: relative; }

  .backdrop {
    position: absolute; inset: 0;
    background:
      radial-gradient(ellipse 300px 220px at 420px 500px, rgba(200,190,150,0.55), transparent 70%),
      radial-gradient(ellipse 400px 300px at 900px 700px, rgba(120,100,85,0.5), transparent 70%),
      radial-gradient(ellipse 350px 260px at 200px 150px, rgba(230,215,190,0.6), transparent 70%),
      linear-gradient(160deg, var(--bg-mid) 0%, var(--bg-dark) 55%, #3a2d24 100%);
  }

  .sidebar {
    position: absolute; left: 66px; top: 0; width: 249px; height: 1000px;
    background: var(--sidebar);
  }
  .brand { position: absolute; top: 172px; left: 0; width: 249px; text-align: center; }
  .brand-name { font-size: 22px; color: #222; letter-spacing: 0.3px; }
  .brand-tagline { font-size: 10.5px; color: #333; margin-top: 2px; }

  .site-nav { position: absolute; left: 38px; top: 264px; list-style: none; }
  .site-nav a { color: var(--nav-ink); text-decoration: none; display: block; }
  .nav-main a { font-size: 14px; line-height: 24px; }
  .nav-group { margin-top: 12px; }
  .nav-group-title { font-size: 18px; line-height: 22px; color: var(--nav-ink); }
  .nav-sub { list-style: none; padding-left: 30px; }
  .nav-sub a { font-size: 13.5px; line-height: 18px; color: #333; }
  .nav-main li:first-child a { font-size: 16px; }

  .tabs { position: absolute; left: 363px; top: 47px; width: 774px; height: 39px; }
  .tab {
    position: absolute; top: 0; height: 39px; color: var(--white);
    font-family: "Quicksand", sans-serif; font-weight: 500; font-size: 23px;
    display: flex; align-items: center; justify-content: center; text-decoration: none;
  }
  .tab-breakfast { left: 0; width: 338px; background: var(--tab-breakfast);
    clip-path: polygon(0 0, 100% 0, 93% 100%, 0 100%); padding-right: 30px; }
  .tab-dinner { left: 314px; width: 270px; background: var(--tab-dinner);
    clip-path: polygon(9% 0, 100% 0, 92% 100%, 0 100%); }
  .tab-lunch { left: 560px; width: 214px; background: var(--tab-lunch);
    clip-path: polygon(10% 0, 100% 0, 100% 100%, 0 100%); padding-left: 16px; }
  .fold { position: absolute; }

  .panel { position: absolute; left: 378px; top: 86px; width: 744px; height: 844px; background: var(--panel); }

  .section-tag {
    position: absolute; left: 363px; top: 137px; width: 293px; height: 38px;
    background: var(--tab-breakfast); color: var(--white);
    clip-path: polygon(0 0, 100% 0, 87% 100%, 0 100%);
    font-family: "Quicksand", sans-serif; font-weight: 500; font-size: 26px;
    display: flex; align-items: center; padding-left: 102px;
  }

  .dish-photo {
    position: absolute; left: 834px; top: 144px; width: 288px; height: 315px;
    background:
      radial-gradient(ellipse 110px 60px at 170px 200px, #e8b070, transparent 70%),
      radial-gradient(ellipse 50px 60px at 60px 70px, #ffc020, transparent 70%),
      linear-gradient(180deg, #fafafa 0%, #f0eeea 100%);
  }

  .menu { position: absolute; left: 467px; top: 208px; width: 330px; }
  .dish-name { color: var(--accent); font-size: 14px; line-height: 20px; }
  .dish-name.small { font-size: 11px; }
  .dish-desc { font-size: 10.5px; line-height: 16px; }
  .dish-price { font-size: 13.5px; line-height: 22px; margin-bottom: -1px; }
  .addons { margin-top: 18px; }
  .addons-title { color: var(--accent); font-size: 14px; line-height: 22px; }
  .addon { font-size: 10.5px; line-height: 22px; white-space: nowrap; }
  .addon b { font-weight: 400; font-size: 13.5px; }
</style>
</head>
<body>
  <div class="backdrop" role="img" aria-label="Softly blurred restaurant interior with table flowers"></div>

  <aside class="sidebar">
    <div class="brand">
      <div class="brand-name">Corrimbel Lodge</div>
      <div class="brand-tagline">restaurant - resort - events</div>
    </div>
    <nav>
      <ul class="site-nav">
        <li>
          <ul class="nav-main" style="list-style:none">
            <li><a href="#">MENU</a></li>
            <li><a href="#">FUNCTIONS</a></li>
            <li><a href="#">RESERVATIONS</a></li>
            <li><a href="#">GALLERY &amp; PRESS</a></li>
            <li><a href="#">CONTACT US</a></li>
          </ul>
        </li>
        <li class="nav-group">
          <span class="nav-group-title">RESORT</span>
          <ul class="nav-sub">
            <li><a href="#">LOFTS &amp; RATES</a></li>
            <li><a href="#">FACILITIES</a></li>
            <li><a href="#">SPECIAL OFFERS</a></li>
            <li><a href="#">GALLERY</a></li>
            <li><a href="#">RESERVATIONS</a></li>
          </ul>
        </li>
        <li class="nav-group">
          <span class="nav-group-title">EVENTS</span>
          <ul class="nav-sub">
            <li><a href="#">WEDDINGS</a></li>
            <li><a href="#">CONFERENCES</a></li>
            <li><a href="#">PRIVATE EVENTS</a></li>
            <li><a href="#">GALLERY</a></li>
            <li><a href="#">ENQUIRY FORM</a></li>
          </ul>
        </li>
      </ul>
    </nav>
  </aside>

  <div class="panel"></div>

  <svg class="fold" style="left:363px;top:86px" width="15" height="18"><polygon points="0,0 15,0 15,18" fill="var(--tab-fold)"/></svg>
  <svg class="fold" style="left:1122px;top:86px" width="15" height="18"><polygon points="0,0 15,0 0,18" fill="var(--tab-fold)"/></svg>
  <svg class="fold" style="left:363px;top:175px" width="15" height="18"><polygon points="0,0 15,0 15,18" fill="var(--tab-fold)"/></svg>

  <nav class="tabs">
    <a class="tab tab-breakfast" href="#">Breakfast</a>
    <a class="tab tab-dinner" href="#">Dinner</a>
    <a class="tab tab-lunch" href="#">Lunch</a>
  </nav>

  <h1 class="section-tag">Breakfast</h1>

  <div class="dish-photo" role="img" aria-label="Breakfast plate with bacon and fried egg, orange juice and coffee cup"></div>

  <section class="menu">
    <div class="dish-name">Corrimbel Lodge Granola</div>
    <div class="dish-desc">Natural Yoghurt &amp; honey</div>
    <div class="dish-price">$13.50</div>

    <div class="dish-name">Buttermilk Pancakes</div>
    <div class="dish-desc">Whipped citrus butter, maple syrup</div>
    <div class="dish-price">$15.50</div>

    <div class="dish-name small">Smoked Bacon, Cheese &amp; Tomato Croissant</div>
    <div class="dish-price">$11.50</div>

    <div class="dish-name">Breakfast Burrito</div>
    <div class="dish-desc">Filled with scrambled egg, bacon, mushroom &amp; sausage,<br>with a tomato &amp; basil salsa and avocado</div>
    <div class="dish-price">$16.50</div>

    <div class="dish-name small">Eggs on Toast</div>
    <div class="dish-desc">Free range eggs, sourdough toast, balsamic roast tomato</div>
    <div class="dish-price">$9.50</div>

    <div class="dish-name">The Vegetarian Breakfast</div>
    <div class="dish-desc">Poached eggs, marinated feta, roast tomato, avocado,<br>kalamata olives, buttered spinach</div>
    <div class="dish-price">$19.50</div>

    <div class="dish-name">The Big Breakfast</div>
    <div class="dish-desc">Free range eggs, sourdough toast, smoked bacon, pork &amp; herb<br>sausage, field mushrooms, balsamic roast tomato, baby spinach</div>
    <div class="dish-price">$19.50</div>

    <div class="dish-name">Eggs Benny Tasting Plate</div>
    <div class="dish-desc">On sourdough toast, double smoked ham, spinach &amp; mushroom,<br>cured Atlantic salmon, topped with hollandaise sauce</div>
    <div class="dish-price">$19.90</div>

    <div class="addons">
      <div class="addons-title">Add Ons:</div>
      <div class="addon">Baby spinach, roast field mushrooms, sauté potato, smoked bacon <b>$3.50</b></div>
      <div class="addon">Double smoked ham, avocado, pork &amp; herb sausage <b>$4.00</b></div>
      <div class="addon">House cured Atlantic salmon <b>$5.00</b></div>
    </div>
  </section>
</body>
</html>
```